Amberline Picture Works Web Design

COMPANY: AMBERLINE PICTURE WORKS
LOCATION: SHANGHAI, CHINA
AREA: FILM/TV DRAMA/COMMERCIALS/GAME POST PRODUCTION, SOUND DESIGN, MUSIC, and GAME.
WEB STYLE: SIMPLE, PROFESSIONAL, TRUSTWORTHY

LANGUAGE: ENGLISH, CHINESE. (Same layout, different language)
UPDATE: AFTER PROJECT FINISHED, WE NEED UPDATE BY OURSELVES.

MAIN SUBJECT: 6
1 HOMEPAGE
2 ABOUT US
3 TEAM
4 SERVICES
5 FACILITY
6 CONTACT

add one page of JOB OPPORTUNITIES.

DETAILS
1 HOMEPAGE
SLOGAN: Amberline Picture Works provides a well-designed working environment which amplifies your team’s ability to reach their creative goals.

Our services include:
 Feature Films
 Music & Scoring
 Commercials
 ADR & Foley
 Sound & Picture Editorial
 Sound Design
 Video Game

2 ABOUT US
Amberline Picture Works is located in the premiere South-Bund area of Shanghai. Occupying a 5000 square meter Technical Building, Amberline Picture Works was built by a filmmaker for filmmakers, and is one of the largest, most versatile full-service post-production facilities in China.

Amberline Picture Works is positioning to be at the forefront of the latest technology. Our goal is to provide a comprehensive solution for the post-production needs of our clients. We offer two fully-equipped dubbing stages (one of which will be certified VORTAN SPHERA ELITE), a large variety of both picture and sound editing rooms, impressive Foley and ADR stages, a world-class scoring stage, and complete audio and video transfer services.

We can handle your entire project from editing all the way to the end of the final sound mix; all under one extremely comfortable roof. We fully realize that the true art is in listening to the needs of our clients and making their greatest vision a reality. To this end our creative team's expertise, with a network of sound supervisors, editors and mixers, will deliver the magic you need. Producers and directors will also find our richly appointed guest accommodations to be a comfortable and soothing place to wind up the day. Every aspect of your project will be taken care of by a skilled and dedicated team, in the way that is best suited to you.

3 TEAM
(attachment 01)

4 SERVICES
Sound Mix
ADR
FOLEY
MUSIC
Sound Design
Sound Edit
Picture Edit
for all the Films, TV Drama, Commercials, Video Games, Online Media
(attachment 02, use photo)

5 FACILITY
(attachment 03)

6 CONTACT
(attachment04)
with map

Reason: Designers work are great, my bosses will spend 1-2 days select one of these web design, and spend 1-2 days to make some change, maybe use new photos.

```html
<!DOCTYPE html>
<html lang="en">
<head>
<meta charset="utf-8">
<title>Amberline Picture Works</title>
<link href="https://fonts.googleapis.com/css2?family=Questrial&family=Montserrat:wght@600&display=swap" rel="stylesheet">
<style>
:root{
  --red:#d3153f;
  --red-dark:#a80f32;
  --ink:#1d1d1e;
  --ink-deep:#141415;
  --bar:#0a0a0b;
  --text:#c9c9c9;
  --muted:#a6a6a6;
  --white:#ffffff;
}
*{margin:0;padding:0;box-sizing:border-box}
html,body{width:676px;height:1200px;overflow:hidden;background:var(--ink)}
body{position:relative;font-family:Arial,Helvetica,sans-serif;color:var(--text)}
.abs{position:absolute}
.header{left:0;top:0;width:676px;height:72px;background:linear-gradient(90deg,#3a0b17,#5a1026 40%,#3b1030)}
.nav-bar{left:0;top:46px;width:676px;height:26px;background:var(--bar)}
.brand{left:57px;top:18px;font-family:Montserrat,sans-serif;font-weight:600;color:var(--white);line-height:23px;font-size:17px;letter-spacing:.5px}
.contact-line{right:57px;font-size:10px;color:var(--white);display:flex;align-items:center;gap:6px}
.contact-phone{top:10px;font-size:13px;color:var(--red)}
.contact-mail{top:29px}
.nav{left:275px;top:46px;display:flex;height:26px}
.nav a{font-size:8px;color:var(--white);text-decoration:none;line-height:26px;padding:0 9px;margin-right:10px;letter-spacing:.2px}
.nav a.active{background:var(--red);margin-right:8px}
.hero{left:0;top:72px;width:676px;height:348px;background:radial-gradient(ellipse at 15% 20%,#8a1230,transparent 55%),radial-gradient(ellipse at 85% 85%,#4b5a8c,transparent 55%),linear-gradient(160deg,#4a0a1f,#2a1436 60%,#3a3c62)}
.hero-frame{left:56px;top:96px;width:564px;height:284px;border:2px solid var(--white);background:linear-gradient(135deg,#4a3a2a,#8a7250 45%,#2a2624)}
.arrow{top:219px}
.section-head{font-family:Questrial,sans-serif;font-size:18px;color:var(--red)}
.films{left:0;top:420px;width:676px;height:280px;background:var(--ink)}
.divider{width:1px;background:#2c2c2d}
.thumb{border:1px solid #555}
.item-title{font-size:10px;font-weight:bold;color:var(--white)}
.item-text{font-size:7.4px;line-height:11.2px;color:var(--muted)}
.btn{font-size:6.5px;color:var(--white);background:var(--red);padding:2px 3px;border-radius:1px}
.music-title{font-size:10px;color:var(--white);width:160px;display:flex;justify-content:space-between;align-items:baseline}
.music-title span{font-size:7px}
.commercial{left:0;top:700px;width:676px;height:190px;background:radial-gradient(ellipse at 50% 60%,#2f2d2a,#101010 70%)}
.game{left:0;top:890px;width:676px;height:242px;background:var(--ink)}
.services li{list-style:none;font-family:Questrial,sans-serif;font-size:9px;color:var(--white);height:19.2px;letter-spacing:.3px}
.services li b{color:var(--red);font-weight:normal;margin-right:2px}
.footer{left:0;top:1132px;width:676px;height:68px;background:var(--red)}
.foot-links{right:57px;font-size:7px;color:var(--white);word-spacing:1px}
</style>
</head>
<body>
<div class="abs header"></div>
<div class="abs nav-bar"></div>
<div class="abs brand">AMBERLINE<br>PICTURE WORKS</div>
<div class="abs contact-line contact-phone">
  <svg width="13" height="13" viewBox="0 0 13 13"><circle cx="6.5" cy="6.5" r="5.8" fill="none" stroke="#fff" stroke-width="1"/><path d="M4.3 3.6c.5-.4.9-.2 1.1.3l.4.9c.1.3 0 .6-.3.8l-.3.2c.3.7.8 1.3 1.5 1.6l.3-.3c.2-.2.5-.3.8-.1l.8.5c.4.3.5.7.1 1.1-.8.8-2 .5-3.1-.6-1.2-1.1-1.9-2.6-1.3-3.4z" fill="#fff"/></svg>
  1800.000.246
</div>
<div class="abs contact-line contact-mail">
  <svg width="14" height="9" viewBox="0 0 14 9"><rect x="3" y=".5" width="10.5" height="8" fill="none" stroke="#fff"/><path d="M3 .5l5.2 4.5 5.3-4.5M0 3h2M0 6h2" fill="none" stroke="#fff"/></svg>
  hello@amberlinepw.com
</div>
<nav class="abs nav">
  <a class="active">HOME</a><a>ABOUT US</a><a>TEAM</a><a>SERVICES</a><a>FACILITY</a><a>CONTACT</a>
</nav>

<div class="abs hero" role="img" aria-label="Blurred concert crowd under red stage lights"></div>
<div class="abs hero-frame" role="img" aria-label="Sound engineer working at a mixing console in a studio"></div>
<svg class="abs arrow" style="left:17px" width="36" height="36" viewBox="0 0 36 36"><circle cx="18" cy="18" r="16" fill="rgba(0,0,0,.25)" stroke="#fff" stroke-width="2.5"/><path d="M23 10l-12 8 12 8-3-8z" fill="#fff"/></svg>
<svg class="abs arrow" style="left:623px" width="36" height="36" viewBox="0 0 36 36"><circle cx="18" cy="18" r="16" fill="rgba(0,0,0,.25)" stroke="#fff" stroke-width="2.5"/><path d="M13 10l12 8-12 8 3-8z" fill="#fff"/></svg>

<section class="abs films"></section>
<h2 class="abs section-head" style="left:57px;top:437px">Feature Films</h2>
<div class="abs thumb" style="left:57px;top:473px;width:139px;height:84px;background:linear-gradient(135deg,#2e2e2e,#6a6a62 50%,#222)" role="img" aria-label="Rack-mounted audio interface with knobs"></div>
<div class="abs item-title" style="left:207px;top:472px">Lorem ipsum dolor sit amet.</div>
<p class="abs item-text" style="left:207px;top:488px;width:200px">Lorem ipsum dolor sit amet, consectetur adipisicing elit, sed do eiusmod tempor incididunt ut labore et dolore magna aliqua. Ut enim ad minim veniam, quis nostrud commodo consequat.</p>
<span class="abs btn" style="left:208px;top:544px">View Detail</span>
<div class="abs thumb" style="left:57px;top:580px;width:139px;height:84px;background:linear-gradient(90deg,#3a2a20,#5b3340 40%,#2a3550 70%,#1f1f22)" role="img" aria-label="Studio hardware panel with coloured buttons"></div>
<div class="abs item-title" style="left:207px;top:579px">Lorem ipsum dolor sit amet.</div>
<p class="abs item-text" style="left:207px;top:595px;width:200px">Lorem ipsum dolor sit amet, consectetur adipisicing elit, sed do eiusmod tempor incididunt ut labore et dolore magna aliqua. Ut enim ad minim veniam, quis nostrud commodo consequat.</p>
<span class="abs btn" style="left:208px;top:651px">View Detail</span>
<div class="abs divider" style="left:433px;top:436px;height:244px"></div>

<h2 class="abs section-head" style="left:456px;top:437px">Music &amp; Scoring</h2>
<div class="abs music-title" style="left:456px;top:470px">Lorem ipsum dolor <span>Dt.03/11/14</span></div>
<p class="abs item-text" style="left:456px;top:485px;width:166px">Lorem ipsum dolor sit amet, consectetur adipisicing elit, sed do eiusmod tempor incididunt ut ullamodo consequat.</p>
<div class="abs music-title" style="left:456px;top:538px">Lorem ipsum dolor <span>Dt.03/11/14</span></div>
<p class="abs item-text" style="left:456px;top:553px;width:166px">Lorem ipsum dolor sit amet, consectetur adipisicing elit, sed do eiusmod tempor incididunt ut ullamodo consequat.</p>
<div class="abs music-title" style="left:456px;top:603px">Lorem ipsum dolor <span>Dt.03/11/14</span></div>
<p class="abs item-text" style="left:456px;top:618px;width:166px">Lorem ipsum dolor sit amet, consectetur adipisicing elit, sed do eiusmod tempor incididunt ut ullamodo consequat.</p>

<section class="abs commercial" role="img" aria-label="Dim mixing desk in the background"></section>
<h2 class="abs section-head" style="left:57px;top:709px;font-family:Arial,sans-serif;font-weight:bold;font-size:17px">Commerical</h2>
<div class="abs thumb" style="left:56px;top:744px;width:136px;height:116px;background:linear-gradient(135deg,#d8d8d8,#6a6a6a 60%,#2a2a2a)" role="img" aria-label="Woman wearing headphones"></div>
<div class="abs thumb" style="left:198px;top:744px;width:136px;height:116px;background:linear-gradient(135deg,#5a3a2c,#b88a72 50%,#3a2620)" role="img" aria-label="Woman with headphones around her neck"></div>
<div class="abs thumb" style="left:341px;top:744px;width:137px;height:116px;background:linear-gradient(135deg,#e0e0e0,#5a8a9a 50%,#1c1c1c)" role="img" aria-label="Person holding a boombox"></div>
<div class="abs thumb" style="left:484px;top:744px;width:136px;height:116px;background:linear-gradient(135deg,#c89030,#3a2a18 55%,#111)" role="img" aria-label="Small audio mixer on a desk"></div>

<section class="abs game"></section>
<h2 class="abs section-head" style="left:57px;top:904px">Video Game</h2>
<div class="abs thumb" style="left:59px;top:937px;width:91px;height:66px;background:radial-gradient(circle at 50% 45%,#8aa050,#1c4a5a 55%,#0a1a22)" role="img" aria-label="Helmeted game character"></div>
<div class="abs item-title" style="left:158px;top:936px">Lorem ipsum dolor sit amet</div>
<p class="abs item-text" style="left:158px;top:951px;width:255px">Lorem ipsum dolor sit amet, consectetur adipisicing elit, sed do eiusmod tempor incididunt ut labore et dolore magna aliqua. commodo consequat. Duis aute irure dolor in reprehenderit.</p>
<span class="abs btn" style="left:160px;top:990px;padding:2px 6px">More</span>
<div class="abs thumb" style="left:59px;top:1021px;width:91px;height:66px;background:radial-gradient(circle at 50% 45%,#8aa050,#1c4a5a 55%,#0a1a22)" role="img" aria-label="Helmeted game character"></div>
<div class="abs item-title" style="left:158px;top:1020px">Lorem ipsum dolor sit amet</div>
<p class="abs item-text" style="left:158px;top:1035px;width:255px">Lorem ipsum dolor sit amet, consectetur adipisicing elit, sed do eiusmod tempor incididunt ut labore et dolore magna aliqua. commodo consequat. Duis aute irure dolor in reprehenderit.</p>
<span class="abs btn" style="left:160px;top:1074px;padding:2px 6px">More</span>
<div class="abs divider" style="left:460px;top:908px;height:200px"></div>

<h2 class="abs section-head" style="left:499px;top:906px">Our Services</h2>
<ul class="abs services" style="left:499px;top:939px">
  <li><b>»</b>Feature Films</li>
  <li><b>»</b>Music &amp; Scoring</li>
  <li><b>»</b>Commercials</li>
  <li><b>»</b>ADR &amp; Foley</li>
  <li><b>»</b>Sound &amp; Picture Editorial</li>
  <li><b>»</b>Sound Design</li>
  <li><b>»</b>Video Game</li>
</ul>

<footer class="abs footer"></footer>
<div class="abs brand" style="top:1142px;line-height:26px;font-size:18px">AMBERLINE<br>PICTURE WORKS</div>
<div class="abs foot-links" style="top:1147px">Home &nbsp;&nbsp;| &nbsp;&nbsp;Featured Artist &nbsp;&nbsp;| &nbsp;&nbsp;Current Auctions &nbsp;&nbsp;| &nbsp;&nbsp;Online Store &nbsp;&nbsp;| &nbsp;&nbsp;Archives &nbsp;&nbsp;| &nbsp;&nbsp;View cart &nbsp;&nbsp;| &nbsp;&nbsp;Contact</div>
<div class="abs foot-links" style="top:1168px">Copyright © 2013, Amberline Picture Works &nbsp;&nbsp;Privacy Policy &nbsp;&nbsp;| &nbsp;&nbsp;Terms &amp; Conditions</div>
</body>
</html>
```